Hi Tech startup needs a Business Card design

We need a business card design for a new company based in Russia called Velturo. We develop innovative telecom solutions for corporation and customers. Our initial product is an Qorvel app that directly connects customers to call centers and help desks via VoIP solutions without the need to dial (800) numbers saving time for customers and saving money for businesses.

We would like to see a design that communicates modern solutions and revolutionary approach. Not too cocky though.

Target Market(s)

the targeted audience is investors, partners, future directors and customers (large corporations)

Industry/Entity Type

Telecom

Requirements
Must have
• standard info

email / phone / plumtalk

```html
<!DOCTYPE html>
<html lang="en">
<head>
<meta charset="UTF-8">
<title>Velturo Business Card</title>
<link href="https://fonts.googleapis.com/css2?family=PT+Sans:wght@400;700&display=swap" rel="stylesheet">
<style>
  :root {
    --page-bg: #1c1c1c;
    --card-bg: #ffffff;
    --ink: #111111;
    --ink-soft: #555555;
    --accent: #ffa500;
    --accent-mark: #f7b500;
    --email: #b8862e;
    --rule: #c8c8c8;
    --faint: #f4f4f4;
  }
  html, body {
    margin: 0;
    padding: 0;
    width: 1200px;
    height: 1034px;
    overflow: hidden;
    background: var(--page-bg);
    font-family: "PT Sans", sans-serif;
  }
  .business-card {
    position: absolute;
    left: 75px;
    top: 217px;
    width: 1050px;
    height: 600px;
    background: var(--card-bg);
    overflow: hidden;
    color: var(--ink);
  }
  .faint-disc {
    position: absolute;
    left: -120px;
    top: 20px;
    width: 450px;
    height: 450px;
    border-radius: 50%;
    background: var(--faint);
  }
  .brand {
    position: absolute;
    left: 239px;
    top: 100px;
    display: flex;
    align-items: center;
    gap: 20px;
  }
  .brand-dot {
    width: 150px;
    height: 150px;
    border-radius: 50%;
    background: var(--accent-mark);
  }
  .brand-name {
    font-size: 104px;
    font-weight: 400;
    line-height: 1;
    color: var(--ink);
    letter-spacing: -1px;
  }
  .person {
    position: absolute;
    left: 0;
    right: 0;
    top: 330px;
    text-align: center;
  }
  .person-name {
    font-size: 40px;
    font-weight: 700;
    line-height: 1.1;
  }
  .person-role {
    font-size: 24px;
    color: var(--ink-soft);
    line-height: 1.1;
  }
  .divider-h {
    position: absolute;
    left: 50px;
    right: 50px;
    top: 416px;
    height: 2px;
    background: var(--rule);
  }
  .divider-v {
    position: absolute;
    left: 524px;
    top: 436px;
    width: 2px;
    height: 128px;
    background: var(--rule);
  }
  .address, .contacts {
    position: absolute;
    top: 440px;
    font-size: 24px;
    line-height: 41px;
  }
  .address { left: 50px; }
  .contacts { right: 50px; text-align: right; }
  .contacts .email { color: var(--email); }
  .address p, .contacts p { margin: 0; }
  .accent-band {
    position: absolute;
    left: 0;
    right: 0;
    bottom: 0;
    height: 21px;
    background: var(--accent);
  }
</style>
</head>
<body>
  <div class="business-card">
    <div class="faint-disc"></div>
    <div class="brand">
      <div class="brand-dot"></div>
      <div class="brand-name">Velturo</div>
    </div>
    <div class="person">
      <div class="person-name">Daniel Harlow</div>
      <div class="person-role">Co-founder</div>
    </div>
    <div class="divider-h"></div>
    <div class="address">
      <p>418, Linden Way</p>
      <p>Ashby Road , suite 5</p>
      <p>Northdale , 190244</p>
    </div>
    <div class="divider-v"></div>
    <div class="contacts">
      <p class="email">hello@velturo.com</p>
      <p>+7 495 210 4418</p>
      <p>www.plumtalk.com/velturo</p>
    </div>
    <div class="accent-band"></div>
  </div>
</body>
</html>
```